Verpackungsdesign für hochwertiges Haarparfum
Zielgruppe
Tovel's Method ist eine israelische Firma, die hochqualitative Haarprodukte und Haar Tools verkauft. Unsere Zielgruppe sind Frauen, die viel in Ihr Aussehen investieren und auf Ihr Äußeres sehr Wert legen.
Aufgabenstellung
Wir suchen nach einem Design für unsere zwei neuen Haarparfums. Es sollte teuer aussehen und das Design sollte modern und simpel sein. Die Flachen sind mit Milchglas und das Design wird auf die Flaschen gedruckt. Das Design muss komplett in Englischer Sprache sein.
Die Masse sind:
Höhe 7,7 cm
Umfang 11 cm
Es wird zwei Düfte geben.
1. The Nordic : Deckel wird Silber glänzend
2. The Celtic: Deckel wird Silber matt
Informationen die auf der Flasche sein sollten:
1. Firmen Logo (wird angehängt)
2. Name des Parfüms (The Nordic or the Celtic)
3. Longlasting Hair Fragrance
4. 30 ml
5. Includes essential hair vitamins and minerals
6. Alcohol and salt free

```html
<!DOCTYPE html>
<html lang="en">
<head>
<meta charset="utf-8">
<title>Tovel's Method – Nordic Hair Fragrance Label</title>
<link href="https://fonts.googleapis.com/css2?family=Cormorant+Garamond:wght@500&family=Source+Serif+4:wght@400&display=swap" rel="stylesheet">
<style>
  :root {
    --backdrop: #eeeeee;
    --label-grey: #999999;
    --label-edge: #111111;
    --print-white: #ffffff;
    --soft-white: #f2f2f2;
    --gold: #f2b51c;
  }
  html, body {
    margin: 0;
    padding: 0;
    width: 1200px;
    height: 895px;
    overflow: hidden;
    background: var(--backdrop);
  }
  .label {
    position: absolute;
    left: 120px;
    top: 19px;
    width: 956px;
    height: 852px;
    background: var(--label-grey);
    border: 2px solid var(--label-edge);
    font-family: "Source Serif 4", Georgia, serif;
    color: var(--print-white);
  }
  .label-art {
    position: absolute;
    left: 0;
    top: 0;
    width: 960px;
    height: 856px;
  }
  .text-block {
    position: absolute;
    text-align: center;
    transform: translateX(-50%);
    white-space: nowrap;
  }
  .brand-mark {
    left: 663px;
    top: 92px;
    display: flex;
    align-items: center;
    gap: 6px;
    font-size: 12px;
    letter-spacing: 1.5px;
    text-transform: uppercase;
  }
  .brand-square {
    width: 10px;
    height: 10px;
    background: var(--print-white);
  }
  .front-panel .overline {
    left: 663px;
    top: 366px;
    font-size: 11px;
    letter-spacing: 2px;
    color: var(--soft-white);
    opacity: .8;
  }
  .front-panel .fragrance-name {
    left: 663px;
    top: 382px;
    font-family: "Cormorant Garamond", Georgia, serif;
    font-weight: 500;
    font-size: 42px;
    letter-spacing: 1px;
    line-height: 1;
  }
  .front-panel .tagline {
    left: 663px;
    top: 470px;
    font-size: 12px;
    letter-spacing: 2px;
    line-height: 16px;
    opacity: .8;
  }
  .front-panel .volume {
    left: 663px;
    top: 758px;
    font-size: 16px;
    letter-spacing: 1px;
  }
  .side-panel .headline {
    left: 226px;
    top: 373px;
    font-size: 16px;
    line-height: 17px;
    letter-spacing: 1px;
  }
  .side-panel .benefit {
    left: 226px;
    top: 437px;
    font-size: 13px;
    line-height: 16px;
  }
  .side-panel .claim {
    left: 226px;
    top: 488px;
    font-size: 13px;
  }
</style>
</head>
<body>
  <div class="label">
    <svg class="label-art" viewBox="0 0 960 856" xmlns="http://www.w3.org/2000/svg">
      <g class="temple-frame" fill="var(--print-white)">
        <rect class="entablature" x="536" y="181" width="253" height="5"/>
        <rect class="column column-left" x="529" y="202" width="64" height="576" role="img" aria-label="Illustrated white Ionic column, left" opacity=".95"/>
        <rect class="column column-right" x="734" y="202" width="64" height="576" role="img" aria-label="Illustrated white Ionic column, right" opacity=".95"/>
        <rect class="stylobate" x="499" y="785" width="328" height="12"/>
      </g>
      <ellipse class="oval-window" cx="663" cy="434" rx="114" ry="181" fill="var(--label-grey)"/>
      <ellipse class="gold-ring" cx="663" cy="434" rx="114" ry="181" fill="none" stroke="var(--gold)" stroke-width="11"/>
      <line class="name-rule" x1="576" y1="431" x2="750" y2="431" stroke="var(--soft-white)" stroke-width="1"/>
      <g class="side-rules" stroke="var(--print-white)" stroke-width="1">
        <line x1="137" y1="430" x2="314" y2="430"/>
        <line x1="137" y1="433" x2="314" y2="433"/>
        <line x1="137" y1="478" x2="314" y2="478"/>
        <line x1="137" y1="481" x2="314" y2="481"/>
      </g>
    </svg>

    <div class="text-block brand-mark"><span class="brand-square"></span>Tovel's Method</div>

    <div class="front-panel">
      <div class="text-block overline">PERFUME</div>
      <div class="text-block fragrance-name">NORDIC</div>
      <div class="text-block tagline">LONGLASTING<br>HAIR FRAGRANCE</div>
      <div class="text-block volume">30 ML</div>
    </div>

    <div class="side-panel">
      <div class="text-block headline">LONGLASTING<br>HAIR FRAGRANCE</div>
      <div class="text-block benefit">Includes essential hair<br>vitamins and minerals</div>
      <div class="text-block claim">Alcohol and salt free</div>
    </div>
  </div>
</body>
</html>
```